Non fiction book cover. The book advises how to get a new job.

The book size will be 20cm high by 13cm wide and I need a front cover which can wrap around to the back. This book has a serious message, but I've tried to make it quite light to read and accessible. So I don't want a cover that is too dour or serious and not frivolous either. At the end of the project, I will need a high resolution 3D image of the book, included as part of the package.<br/>The Title of the book is:- "Past Your Prime? Hunting for the Next Role?<br/>by Gerald Whitcombe-Prynne".<br/>I am thinking of a light yellow background, with a striking image to attract attention. The image and words should be clear and sharp.<br/>Here is the, BACK COVER wording.<br/>"This book tells you clearly and simply the steps that you need to take, to get a job, once you’re over 50.<br/>It advises you on the techniques to use to write a killer CV.<br/>It explains how to ensure that your CV attention.<br/>It shows the best way to approach your local job agency.<br/>It demonstrates the best way to use your network.<br/><br/>This book, written by someone with 30 years’ experience in the recruitment industry, gives you ALL the answers.<br/>Whether you are a top executive or someone after some local part time work, then this book is for you. <br/>With the help of this book you will secure your next position.<br/>

Target Market(s)

UK, over 50s, male and female.

Font styles to use
Serif

Colors
fbee3e

Requirements
Must have
• A clear uncluttered cover.
Should not have
• Fussy and over complicated

```html
<!DOCTYPE html>
<html lang="en">
<head>
<meta charset="utf-8">
<title>Past Your Prime? – Book Cover Wrap</title>
<link rel="stylesheet" href="https://fonts.googleapis.com/css2?family=Arimo:wght@400;500;700&display=swap">
<style>
  :root {
    --paper: #ffffff;
    --cover-yellow: #f0e11f;
    --ink-green: #273a30;
    --ink-black: #111111;
    --photo-dark: #3a3a3a;
    --photo-mid: #7a7a7a;
    --photo-light: #d6d6d6;
    --mark-yellow: #f9ec3a;
  }
  * { margin: 0; padding: 0; box-sizing: border-box; }
  html, body { width: 1200px; height: 1200px; overflow: hidden; background: var(--paper); }
  body { position: relative; font-family: "Arimo", Arial, sans-serif; }

  .cover { position: absolute; top: 16px; width: 577px; height: 886px; background: var(--cover-yellow); overflow: hidden; }
  .cover--front { left: 16px; }
  .cover--back { left: 614px; }

  .front-title-top {
    position: absolute; left: 16px; top: 84px; width: 550px;
    display: flex; justify-content: space-between;
    font-size: 150px; line-height: 1; font-weight: 400; color: var(--ink-green);
  }
  .front-title-side {
    position: absolute; right: 16px; top: 238px; text-align right; text-align: right; color: var(--ink-green);
  }
  .front-title-side .word-small { display: block; font-size: 44px; line-height: 1; letter-spacing: 2px; }
  .front-title-side .word-large { display: block; font-size: 82px; line-height: 1; letter-spacing: -3px; margin-top: 4px; }
  .front-subtitle {
    position: absolute; left: 20px; top: 280px; width: 220px;
    font-size: 25px; line-height: 31px; font-weight: 400; color: var(--ink-green); letter-spacing: 0.3px;
  }
  .front-author {
    position: absolute; right: 10px; top: 423px; font-size: 12.5px; color: var(--ink-green);
  }
  .front-photo {
    position: absolute; left: 0; top: 444px; width: 577px; height: 442px;
    background: linear-gradient(115deg, var(--photo-dark) 0%, var(--photo-mid) 35%, var(--photo-light) 55%, var(--photo-mid) 75%, var(--photo-dark) 100%);
  }

  .back-headline {
    position: absolute; left: 0; top: 182px; width: 100%; text-align: center;
    font-size: 27px; line-height: 32px; font-weight: 500; color: var(--ink-black);
  }
  .back-points {
    position: absolute; left: 62px; top: 390px; list-style: none;
    font-size: 17px; line-height: 28.5px; color: var(--ink-black);
  }
  .back-points li::before { content: "\2731"; font-size: 11px; margin-right: 9px; position: relative; top: -2px; }
  .back-blurb {
    position: absolute; left: 40px; top: 608px; width: 500px; text-align: center;
    font-size: 14px; line-height: 19px; color: var(--ink-black);
  }

  .publisher {
    position: absolute; left: 0; top: 1040px; width: 100%;
    display: flex; justify-content: center; align-items: center; gap: 14px;
    font-size: 34px; font-weight: 700; color: var(--mark-yellow);
  }
  .publisher-dot { width: 40px; height: 40px; border-radius: 50%; background: var(--mark-yellow); }
</style>
</head>
<body>
  <section class="cover cover--front">
    <h1 class="front-title-top" aria-label="Past"><span>P</span><span>A</span><span>S</span><span>T</span></h1>
    <div class="front-title-side">
      <span class="word-small">YOUR</span>
      <span class="word-large">PRIME?</span>
    </div>
    <p class="front-subtitle">HUNTING FOR<br>THE NEXT<br>ROLE?</p>
    <p class="front-author">by Gerald Whitcombe-Prynne</p>
    <div class="front-photo" role="img" aria-label="Black and white photograph of a businessman's hand extended for a handshake"></div>
  </section>

  <section class="cover cover--back">
    <p class="back-headline">This book tells you clearly and simply<br>the steps that you need to take,<br>to get a job, once you’re over 50.</p>
    <ul class="back-points">
      <li>It advises you on the techniques to use to write a killer CV.</li>
      <li>It explains how to ensure that your CV attention.</li>
      <li>It shows the best way to approach your local job agency.</li>
      <li>It demonstrates the best way to use your network.</li>
    </ul>
    <p class="back-blurb">This book, written by someone with 30 years’ experience in the recruitment industry, gives you ALL the answers. Whether you are a top executive or someone after some local part time work, then this book is for you. With the help of this book you will secure your next position.</p>
  </section>

  <div class="publisher"><span class="publisher-dot"></span><span>Stride Books</span></div>
</body>
</html>
```